Flyer-Design für Eröffnung des Salons Belle Rivane gesucht
Zielgruppe
Es soll sehr gut mit meinem Website harmonisieren.
www.belle-rivane.ch
Aufgabenstellung
Ich eröffne einen Kosmetiksalon und wünsche mir einen schönen Flyer zur Ankündigung der Eröffnung. Bitte in A5 im Hochformat erstellen.
Der Flyer soll auch einen Gutschein für eine Gesichtsbehandlung im Wert von 30 Chf enthalten (nach Möglichkeit rechts oben auf dem Flyer, in einer gut sichtbaren Farbe).
Auf den Seiten des Flyers wünsche ich einfache Abschlüsse mit sanften Farben oder in Schwarz-weissem Grauton Blumendesign.
Der ganze Flyer soll eher simple wirken und dennoch ein Blickfang sein,darf nicht kitschig auffallen sondern soll Klasse und Edel wirken.
Mittig soll Platz sein fur vier Linien Text,d.h ein noch nicht ganz definiertes Angebot für drei Arten von Gesichtsbehandlungen und eiem speziellen Angebot. Im moment können noch Fantasietexte als Platzhalter dienen.

```html
<!DOCTYPE html>
<html lang="de">
<head>
<meta charset="utf-8">
<title>Belle Rivane – Neueröffnung Flyer</title>
<link rel="stylesheet" href="https://fonts.googleapis.com/css2?family=Jost:wght@400;500;600;700&display=swap">
<style>
  :root {
    --sky: #7fcbe0;
    --sky-text: #62bedb;
    --voucher: #b7dee7;
    --taupe: #a69890;
    --taupe-dark: #8a7d76;
    --body-grey: #8f8580;
    --paper: #ffffff;
  }
  * { box-sizing: border-box; margin: 0; padding: 0; }
  html, body { width: 1200px; height: 848px; overflow: hidden; background: var(--paper); }
  body { position: relative; font-family: "Jost", "Futura", sans-serif; }

  .page {
    position: absolute; top: 117px; width: 423px; height: 600px;
    background: var(--paper); overflow: hidden;
    box-shadow: 0 0 3px rgba(0,0,0,.25);
  }
  .page--front { left: 138px; }
  .page--menu { left: 632px; }

  /* Front */
  .headline-band {
    position: absolute; left: 0; top: 0; width: 100%; height: 53px;
    background: var(--sky); display: flex; align-items: center; justify-content: center;
  }
  .headline {
    color: #fff; font-weight: 600; font-size: 40px; letter-spacing: 3px; line-height: 1;
    margin-left: -16px;
  }
  .hero-photo {
    position: absolute; left: 0; top: 53px; width: 100%; height: 400px;
    background:
      linear-gradient(180deg, rgba(255,255,255,0) 70%, #fff 100%),
      linear-gradient(120deg, #f1ede6 0%, #e8cdb9 30%, #5a4336 48%, #e9c9b2 62%, #f4f1ee 85%);
  }
  .voucher {
    position: absolute; left: 17px; top: 425px; width: 194px; height: 194px;
    border-radius: 50%; background: var(--voucher);
    border: 2px solid #fff; box-shadow: 2px 3px 6px rgba(0,0,0,.3);
  }
  .voucher__value {
    position: absolute; left: 0; width: 100%; top: 28px; text-align: center;
    color: var(--taupe); font-weight: 700; font-size: 36px; letter-spacing: 2px; line-height: 1;
  }
  .voucher__label {
    position: absolute; left: 24px; top: 68px; width: 146px; height: 20px;
    background: var(--taupe); color: #fff; font-weight: 600; font-size: 15px;
    letter-spacing: 1px; text-align: center; line-height: 20px;
    box-shadow: 2px 2px 3px rgba(0,0,0,.3);
  }
  .voucher__line {
    position: absolute; left: 25px; width: 145px; height: 1px; background: #fff;
  }

  .brand { position: absolute; color: var(--taupe); font-weight: 400; white-space: nowrap; display: flex; align-items: center; gap: 8px; }
  .brand__dot { border-radius: 50%; background: var(--voucher); flex: none; }
  .brand--front { left: 232px; top: 450px; font-size: 30px; }
  .brand--front .brand__dot { width: 14px; height: 14px; }
  .site-url { position: absolute; color: var(--taupe); letter-spacing: 2px; white-space: nowrap; }
  .site-url--front { left: 245px; top: 497px; font-size: 7px; }

  .contact {
    position: absolute; left: 245px; top: 518px; color: var(--taupe-dark);
    font-size: 10px; line-height: 13px; font-style: normal;
  }
  .contact strong { font-weight: 600; }

  /* Menu */
  .menu { position: absolute; left: 14px; top: 12px; width: 396px; }
  .menu__section { color: var(--taupe-dark); font-weight: 600; font-size: 15px; line-height: 18px; }
  .treatment { margin-top: 8px; }
  .treatment__head, .service {
    display: flex; justify-content: space-between; font-weight: 600; line-height: 17px;
  }
  .treatment__head { color: var(--sky-text); font-size: 15px; }
  .treatment__desc {
    color: var(--body-grey); font-size: 9px; line-height: 12px; text-align: justify;
    text-transform: uppercase;
  }
  .services { margin-top: 20px; }
  .service { color: var(--taupe-dark); font-size: 15px; margin-bottom: 11px; }
  .service__price { color: var(--sky-text); }

  .brand--menu { left: 15px; top: 492px; font-size: 46px; }
  .brand--menu .brand__dot { width: 22px; height: 22px; }
  .site-url--menu { left: 45px; top: 562px; font-size: 10px; }

  .partners { position: absolute; left: 295px; top: 533px; width: 116px; height: 44px; }
  .partner-badge { position: absolute; background: #cfc8c3; border-radius: 2px; }
</style>
</head>
<body>

<section class="page page--front">
  <div class="headline-band"><h1 class="headline">NEUERÖFFNUNG</h1></div>
  <div class="hero-photo" role="img" aria-label="Foto: Kosmetikerin massiert sanft Kopf und Hals einer entspannt liegenden Kundin auf weissem Tuch"></div>

  <div class="voucher">
    <div class="voucher__value">30 CHF</div>
    <div class="voucher__label">GUTSCHEIN FÜR</div>
    <div class="voucher__line" style="top:110px"></div>
    <div class="voucher__line" style="top:131px"></div>
    <div class="voucher__line" style="top:152px"></div>
  </div>

  <div class="brand brand--front"><span class="brand__dot"></span>Belle Rivane</div>
  <div class="site-url site-url--front">WWW.BELLE-RIVANE.CH</div>

  <address class="contact">
    <strong>MIRELA DOVANSKA</strong><br>
    <strong>KOSMETIKERIN</strong><br>
    LINDENWEG 12B<br>
    8465 TALWIL<br>
    <strong>TELEFON: 079-318-2260</strong>
  </address>
</section>

<section class="page page--menu">
  <div class="menu">
    <h2 class="menu__section">GESICHTSBEHANDLUNGEN</h2>

    <div class="treatment">
      <div class="treatment__head"><span>KURZBEHANDLUNG</span><span>99 CHF</span></div>
      <p class="treatment__desc">Reinigung, Peeling, Ausreinigung, Augenbrauenkorrektur, beruhigende Maske, Abschlusspflege.</p>
    </div>
    <div class="treatment">
      <div class="treatment__head"><span>KLASSISCHE GESICHTSBEHANDLUNG</span><span>129 CHF</span></div>
      <p class="treatment__desc">Reinigung, Peeling (mit oder ohne Dampf), Ausreinigung, Brauenkorrektur, Essencen-Massage, Mask, Abschlusspflege.</p>
    </div>
    <div class="treatment">
      <div class="treatment__head"><span>SOIN THALASSO</span><span>139 CHF</span></div>
      <p class="treatment__desc">Feuchtigkeitsbehandlung mit vitalisierender Algenmaske Reinigung, Peeling, Ausreinigung, Essence-Massage, Algenmaske, Abschlusspflege.</p>
    </div>
    <div class="treatment">
      <div class="treatment__head"><span>ANTI-AGING BEHANDLUNG</span><span>149 CHF</span></div>
      <p class="treatment__desc">Reinigung, Enzympeeling, Ausreinigung, Brauenkorrektur, Caviar Essence, Massage, Trüffelmaske, Abschlusspflege.</p>
    </div>

    <div class="services">
      <div class="service"><span>HAARENTFERNUNG ab</span><span class="service__price">149 CHF</span></div>
      <div class="service" style="margin-bottom:15px"><span>KOSMETISCHE FUSSPFLEGE ab</span><span class="service__price">30 CHF</span></div>
      <div class="service"><span>WIMPERNVERLÄNGERUNG ab</span><span class="service__price">119 CHF</span></div>
      <div class="service"><span>BEAUTY FOR MEN ab</span><span class="service__price">39 CHF</span></div>
    </div>
  </div>

  <div class="brand brand--menu"><span class="brand__dot"></span>Belle Rivane</div>
  <div class="site-url site-url--menu">WWW.BELLE-RIVANE.CH</div>

  <div class="partners" aria-label="Partnermarken">
    <div class="partner-badge" style="left:28px;top:0;width:88px;height:12px"></div>
    <div class="partner-badge" style="left:0;top:24px;width:54px;height:16px"></div>
    <div class="partner-badge" style="left:68px;top:24px;width:48px;height:16px"></div>
  </div>
</section>

</body>
</html>
```